Business Card Design Project

We need a business card design for a new company based in Singapore called 'Bright Harbor Pte Ltd'. We provide personal development training and emotional intelligence workshops. Our slogan is "Actualize your potentials". We will not have a company address on the business card. Only phone number, email address and website address.

Target Market(s)

Adults age 25 to 45 years old.
Mostly working in a job.

Industry/Entity Type

Training

Colors
0255a2
f37123

```html
<!DOCTYPE html>
<html lang="en">
<head>
<meta charset="utf-8">
<title>Bright Harbor Pte Ltd — Business Card</title>
<link rel="stylesheet" href="https://fonts.googleapis.com/css2?family=Exo+2:wght@400;500;600&display=swap">
<style>
  :root {
    --page-bg: #e6e4e0;
    --brand-blue: #0255a2;
    --brand-orange: #f37123;
    --blue-light: #0aa0ec;
    --blue-mid: #1677d0;
    --card-white: #f4f4f4;
    --arc-grey: #9a9a9a;
    --text-light: #ffffff;
    --logo-blue: #0d6fc4;
  }
  html, body {
    margin: 0;
    width: 1200px;
    height: 900px;
    overflow: hidden;
    background: var(--page-bg);
    font-family: "Exo 2", sans-serif;
  }
  .business-card {
    position: absolute;
    left: 100px;
    top: 164px;
    width: 1000px;
    height: 572px;
    box-shadow: 0 14px 30px rgba(0,0,0,0.25);
    overflow: hidden;
  }
  .card-shapes {
    position: absolute;
    inset: 0;
  }
  .contact-panel {
    position: absolute;
    left: 66px;
    top: 62px;
    color: var(--text-light);
  }
  .holder-name {
    margin: 0;
    font-size: 31px;
    font-weight: 500;
    letter-spacing: 1.5px;
    text-transform: uppercase;
  }
  .holder-title {
    margin: 4px 0 0 4px;
    font-size: 20px;
    font-weight: 400;
  }
  .contact-list {
    list-style: none;
    margin: 70px 0 0 -20px;
    padding: 0;
    font-size: 20px;
  }
  .contact-list li {
    display: flex;
    align-items: center;
    gap: 12px;
    height: 38px;
    letter-spacing: 1px;
  }
  .contact-list li.small {
    font-size: 18px;
    letter-spacing: 0.3px;
  }
  .contact-icon {
    width: 20px;
    height: 20px;
    flex: none;
  }
  .brand-block {
    position: absolute;
    left: 540px;
    top: 262px;
  }
  .brand-name {
    display: flex;
    align-items: center;
    gap: 14px;
    margin: 0;
    color: var(--logo-blue);
    font-size: 42px;
    font-weight: 500;
    letter-spacing: 2px;
    text-transform: uppercase;
  }
  .brand-dot {
    width: 22px;
    height: 22px;
    border-radius: 50%;
    background: var(--brand-orange);
  }
  .brand-slogan {
    margin: 8px 0 0 38px;
    color: var(--brand-orange);
    font-size: 20px;
    font-weight: 500;
    letter-spacing: 1px;
  }
</style>
</head>
<body>
  <div class="business-card">
    <svg class="card-shapes" width="1000" height="572" viewBox="0 0 1000 572" aria-hidden="true">
      <defs>
        <radialGradient id="blueGlow" cx="0.3" cy="0.45" r="0.7">
          <stop offset="0" stop-color="var(--blue-light)"/>
          <stop offset="0.55" stop-color="var(--blue-mid)"/>
          <stop offset="1" stop-color="var(--brand-blue)"/>
        </radialGradient>
      </defs>
      <rect class="blue-field" width="1000" height="572" fill="url(#blueGlow)"/>
      <circle class="white-field" cx="960" cy="360" r="540" fill="var(--card-white)"/>
      <path class="grey-arc" d="M512,80 A528,528 0 0 0 464,540 A780,780 0 0 1 512,80 Z" fill="var(--arc-grey)"/>
    </svg>

    <div class="contact-panel">
      <h1 class="holder-name">Daniel Morrow</h1>
      <p class="holder-title">Managing Director</p>
      <ul class="contact-list">
        <li>
          <svg class="contact-icon" viewBox="0 0 20 20"><path d="M5 2l3 4-2 2c1 2 3 4 5 5l2-2 4 3-2 3C8 16 4 12 3 4z" fill="#fff"/></svg>
          010 555 0142
        </li>
        <li>
          <svg class="contact-icon" viewBox="0 0 20 20"><rect x="5" y="1" width="10" height="18" rx="2" fill="none" stroke="#fff" stroke-width="2"/><circle cx="10" cy="15.5" r="1.2" fill="#fff"/></svg>
          010 555 0143
        </li>
        <li>
          <svg class="contact-icon" viewBox="0 0 20 20"><rect x="2" y="8" width="16" height="10" fill="#fff"/><rect x="5" y="2" width="8" height="6" fill="none" stroke="#fff" stroke-width="2"/></svg>
          010 555 0144
        </li>
        <li class="small">
          <svg class="contact-icon" viewBox="0 0 20 20"><rect x="1" y="4" width="18" height="12" fill="#fff"/><path d="M1 4l9 7 9-7" fill="none" stroke="#0a6cc6" stroke-width="1.5"/></svg>
          hello@brightharbor.sg
        </li>
        <li class="small">
          <svg class="contact-icon" viewBox="0 0 20 20"><circle cx="10" cy="10" r="8" fill="none" stroke="#fff" stroke-width="1.8"/><ellipse cx="10" cy="10" rx="3.5" ry="8" fill="none" stroke="#fff" stroke-width="1.5"/><path d="M2 10h16" stroke="#fff" stroke-width="1.5"/></svg>
          www.brightharbor.sg
        </li>
      </ul>
    </div>

    <div class="brand-block">
      <p class="brand-name"><span class="brand-dot"></span>Bright Harbor</p>
      <p class="brand-slogan">Actualize your potentials</p>
    </div>
  </div>
</body>
</html>
```